Brightwell Giving Inc

We need a full re-design of our non-profit organization website (www.brightwellgiving.org). Ideally, we are looking to make it more attractive, user-friendly, and interactive with our business model.

Please make sure to user colors that ago with our logo.

We need a homepage done and we also need a content page done where we will use for the other pages to fill with content.

Target Market(s)

Clothes/textiles donations.

Industry/Entity Type

Charity

Number of Pages Required

2 page

Colors

Designer to choose colors to be used in the design.

Requirements
Must have
• It must match the styling of our logo and same colors as current website. (www.brightwellgiving.org)
Nice to have
• Sleek homepage that is easy to understand and get our main points across.

```html
<!DOCTYPE html>
<html lang="en">
<head>
<meta charset="utf-8">
<title>Brightwell Giving – Home</title>
<link rel="stylesheet" href="https://fonts.googleapis.com/css2?family=Montserrat:wght@400;600;700&family=Open+Sans:wght@400;600&family=Dancing+Script:wght@400&display=swap">
<style>
:root{
  --green:#5f9a45;
  --green-dark:#3f6a2c;
  --green-soft:#a9c98a;
  --lime:#b8d23c;
  --orange:#d98b14;
  --red:#b7321c;
  --yellow:#f1dc86;
  --yellow-band:#e5c72a;
  --gold:#f7cd1b;
  --card:#b58a5c;
  --ink:#3c3a2e;
  --white:#ffffff;
  --search:#c4301d;
}
*{box-sizing:border-box;margin:0;padding:0}
html,body{width:1200px;height:2198px;overflow:hidden;background:var(--white)}
body{font-family:"Open Sans",Arial,sans-serif;color:var(--white);position:relative}
.site{position:absolute;left:149px;top:7px;width:881px;height:2049px;overflow:hidden}
.abs{position:absolute}
.btn{position:absolute;display:flex;align-items:center;justify-content:center;font-family:"Montserrat",sans-serif;font-weight:600;font-size:14px;letter-spacing:.5px;color:var(--white);border:1.5px solid var(--white);border-radius:3px}
.btn--solid{background:var(--green)}
.btn--ghost{background:transparent}

/* header */
.header{top:0;left:0;width:881px;height:69px;background:var(--green)}
.brand{left:19px;top:10px;display:flex;align-items:center;gap:10px}
.brand__mark{width:44px;height:44px;border-radius:50%;background:var(--gold)}
.brand__name{font-family:"Montserrat",sans-serif;font-weight:700;font-size:19px;color:var(--ink);line-height:1.05}
.brand__tag{font-family:"Montserrat",sans-serif;font-weight:700;font-size:11px;color:var(--ink);display:block}
.nav{top:36px;font-family:"Montserrat",sans-serif;font-weight:600;font-size:12.5px;letter-spacing:1px;color:#2f4a22}
.nav--donate{left:727px;top:29px;width:113px;height:27px;background:var(--gold);border-radius:3px;display:flex;align-items:center;justify-content:center;color:#5a4a10;font-family:"Montserrat",sans-serif;font-weight:600;font-size:12.5px;letter-spacing:1px}

/* hero */
.hero{top:69px;left:0;width:881px;height:442px;background:linear-gradient(160deg,#8a7058 0%,#5b4a3e 40%,#3c3f3a 75%,#2e3531 100%)}
.hero__title{left:57px;top:208px;font-family:"Montserrat",sans-serif;font-weight:700;font-size:39px;line-height:48px;text-shadow:0 2px 4px rgba(0,0,0,.35)}
.dots{left:403px;top:424px;display:flex;gap:8px}
.dots span{width:10px;height:10px;border:1.5px solid var(--white);border-radius:50%}

/* panels */
.panel{top:511px;height:440px}
.panel--giving{left:0;width:440px;background:linear-gradient(180deg,#c44a2c,#a5301d 60%,#b8432a)}
.panel--power{left:440px;width:441px;background:linear-gradient(180deg,#7aa35c,#5d8f4a 60%,#6f9a56)}
.band{position:absolute;top:14px;left:0;width:100%;height:65px;padding:8px 30px;font-family:"Montserrat",sans-serif;font-weight:700;font-size:17px;line-height:30px;text-transform:uppercase}
.band--orange{background:rgba(217,139,20,.9)}
.band--lime{background:rgba(184,210,60,.9);padding-left:32px}
.copy{position:absolute;font-size:13.5px;line-height:20.5px}
.focus{position:absolute;left:44px;top:258px;list-style:none;font-family:"Montserrat",sans-serif;font-weight:700;font-size:15px;line-height:26.5px}

/* trifle */
.trifle-head{top:951px;left:0;width:881px;height:44px;background:#8cb763;font-family:"Montserrat",sans-serif;font-weight:700;font-size:22px;line-height:44px;padding-left:30px;text-transform:uppercase}
.trifle{top:995px;left:0;width:881px;height:326px;background:linear-gradient(180deg,#efd97e,#e8d17a 60%,#d9c274);color:#6b6247}
.trifle .copy{color:#6b6247;font-size:13px;line-height:21px}

/* projects */
.projects-head{top:1321px;left:0;width:881px;height:43px;background:var(--yellow-band);font-family:"Montserrat",sans-serif;font-weight:700;font-size:22px;line-height:43px;text-align:center;letter-spacing:1px}
.projects{top:1364px;left:0;width:881px;height:411px;background:linear-gradient(180deg,#b3cf95,#a6c68a)}
.card{position:absolute;top:22px;width:258px;height:294px;background:var(--card)}
.card__media{position:absolute;left:19px;top:17px;width:221px;height:125px}
.card__title{position:absolute;top:152px;width:100%;text-align:center;font-family:"Montserrat",sans-serif;font-weight:700;font-size:13.5px;letter-spacing:.8px;text-transform:uppercase}
.card__text{position:absolute;left:19px;top:174px;width:222px;font-size:9.6px;line-height:13px}
.card .btn{top:257px;left:87px;width:84px;height:27px;font-size:11.5px}

/* footer */
.footer{top:1775px;left:0;width:881px;height:274px;background:var(--green)}
.footer h3{position:absolute;top:23px;font-family:"Montserrat",sans-serif;font-weight:700;font-size:15.5px;letter-spacing:1px;color:#2e4a22;text-transform:uppercase}
.links{position:absolute;top:46px;list-style:none;font-size:11px;line-height:14px;letter-spacing:.4px;color:#2f4d23}
.quote{left:132px;top:117px;font-family:"Dancing Script",cursive;font-size:27px;line-height:25px;color:#2f4d23;width:460px}
.zip{left:606px;top:47px;width:160px;height:22px;background:var(--white);color:#999;font-size:10px;line-height:22px;padding-left:24px}
.search{left:766px;top:47px;width:61px;height:22px;background:var(--search);font-size:11px;line-height:22px;text-align:center}
.phone{left:606px;font-family:"Montserrat",sans-serif;font-weight:700;font-size:15.5px;letter-spacing:.8px;color:#2e4a22}
.social{left:609px;top:163px;display:flex;gap:5px}
.social span{width:34px;height:34px;border-radius:50%;background:#8ec16d}
.rule{left:50px;top:215px;width:781px;height:1px;background:#4a7a35}
.legal{left:0;top:240px;width:881px;text-align:center;font-size:6.5px;font-weight:600;color:#2f4d23}
</style>
</head>
<body>
<div class="site">

  <header class="abs header">
    <div class="abs brand">
      <span class="brand__mark"></span>
      <div class="brand__name">Brightwell Giving<span class="brand__tag">Think Globally while Donating Locally</span></div>
    </div>
    <span class="abs nav" style="left:363px">HOME</span>
    <span class="abs nav" style="left:433px">ABOUT US</span>
    <span class="abs nav" style="left:530px">OUR MISSION</span>
    <span class="abs nav" style="left:649px">CONTACT</span>
    <span class="abs nav--donate">DONATE</span>
  </header>

  <section class="abs hero" role="img" aria-label="Photo of smiling children reaching toward the camera">
    <h1 class="abs hero__title">Let’s Change Our Community First,<br>World Will Change Automatically...</h1>
    <span class="btn btn--ghost" style="left:313px;top:351px;width:100px;height:32px">Learn More</span>
    <span class="btn btn--solid" style="left:442px;top:351px;width:101px;height:32px">Donate</span>
    <div class="abs dots"><span></span><span></span><span></span><span></span><span></span></div>
  </section>

  <section class="abs panel panel--giving" role="img" aria-label="Photo of a child tinted red">
    <h2 class="band band--orange">“It’s not how much we give but how much love we put into giving.”</h2>
    <p class="copy" style="left:44px;top:120px;width:352px">Our goal is with and within the community.In such trying times as these, the only people we can turn to for help are each other. Nothing is greater than the desire of a community to help its own. Brightwell Giving is dedicated to becoming an active member of the community by providing for its less fortunate members. A non-profit organization is only effective when it benefits the people that need it most. With your help, we can accomplish that goal. Brightwell Giving aims to bring back the spirit of giving to our community, one family at a time...</p>
    <span class="btn btn--ghost" style="left:168px;top:356px;width:101px;height:33px">Learn More</span>
  </section>

  <section class="abs panel panel--power" role="img" aria-label="Photo of a child tinted green">
    <h2 class="band band--lime">Your donations have the power to lightenup the hopes for living.</h2>
    <p class="copy" style="left:44px;top:120px;width:360px">We help communities to stay strong in situations they lose everything. It canot be dones without help of people like yourself. We dream a planet of joy brotherhood and happiness. We help everyone, every right cause.Our strong areas of dfocus are:</p>
    <ul class="focus">
      <li>- SUPPORT ANTI-GUN VIOLENCE</li>
      <li>- HELP DISASTER VICTIMS OF HURRICANE IRENE</li>
      <li>- HELP NORTHLAND FAMILY &amp; CHILD SOCIETY</li>
    </ul>
    <p class="copy" style="left:53px;top:338px;font-size:13px">We will achieve more world atarting with our community.</p>
    <span class="btn btn--solid" style="left:118px;top:356px;width:101px;height:33px">Donate</span>
  </section>

  <h2 class="abs trifle-head">The charity that is a trifle to us can be precious to others.</h2>
  <section class="abs trifle" role="img" aria-label="Faded photo of volunteers standing before a storefront, under a yellow tint">
    <p class="copy" style="left:32px;top:14px;width:382px">Recycling your old clothing is a significant humanitarian act. Brightwell Giving works towards simplifying the collection process by providing practical solutions for waste reduction. Brightwell Giving is particularly qualified to assure an effort for an outstanding clothing recovery initiative. "If your organization is a church, community center, an educational facility or a fitness center", we can arrange for your clothing drop boxes to be placed in your facility, get the word out about the "clothing collection event; retain the clothing afterwards," and distribute the donations to the proper channels, so minimal amount goes to waste.</p>
    <p class="copy" style="left:455px;top:14px;width:375px">Strangely, charity sometimes gets dismissed, as if it is ineffective, inappropriate or even somehow demeaning to the recipient. 'This isn't charity,' some donors take pains to claim, 'This is an investment.' Let us recognize charity for what it is at heart: a noble enterprise aimed at bettering the human condition.<br>If you can afford to donate a small amount for people in need you can directly donate to us which wil be distributed to the people in need. We are open book organization, wewill proide every investment to to you the people.</p>
    <span class="btn btn--ghost" style="left:336px;top:262px;width:100px;height:32px">Learn More</span>
    <span class="btn btn--solid" style="left:447px;top:262px;width:100px;height:32px">Donate</span>
  </section>

  <h2 class="abs projects-head">RECENT PROJECTS</h2>
  <section class="abs projects" role="img" aria-label="Faint map of the Americas and the Caribbean">
    <article class="card" style="left:31px">
      <div class="card__media" role="img" aria-label="Video still about an agriculture school" style="background:linear-gradient(180deg,#2a2a2a,#111)"></div>
      <h3 class="card__title">Agriculture School in Haiti</h3>
      <p class="card__text">Harvest Skills Centre (H.S.C) is a non Governmental Organisation. Where young adult students can learn how to produce foods including vegetables and grow plants to protect the environment.</p>
      <span class="btn btn--ghost">Learn More</span>
    </article>
    <article class="card" style="left:304px">
      <div class="card__media" role="img" aria-label="Photo of a family seated at a table" style="background:linear-gradient(160deg,#c9b3a0,#7a6a62)"></div>
      <h3 class="card__title">Aid to Families</h3>
      <p class="card__text" style="text-align:center">Brought humanitarian aid to large families. Glory to the Lord for the opportunity. Social assistance is the door to the preaching of the gospel. By giving no one has ever been poor rather becae more loved and respected.</p>
      <span class="btn btn--ghost">Learn More</span>
    </article>
    <article class="card" style="left:577px">
      <div class="card__media" role="img" aria-label="Photo of a mother and daughter on a sofa" style="background:linear-gradient(160deg,#8a6a58,#d8cfc2)"></div>
      <h3 class="card__title">Charty for Elena</h3>
      <p class="card__text">Our mutual efforts were able to gather enough monies to provide funds for rehabilitation clinic for Elena in Ukraine. Who was suffering from genetic diesease. From your efforts and ddonation we able to bring back happiness to elena's family</p>
      <span class="btn btn--ghost">Learn More</span>
    </article>
    <span class="btn btn--ghost" style="left:377px;top:348px;width:125px;height:27px;font-size:11px">See More Projects</span>
  </section>

  <footer class="abs footer">
    <h3 style="left:50px">About Us</h3>
    <ul class="links" style="left:56px"><li>About</li><li>Our Mission</li><li>News</li><li>Events</li><li>Blog</li><li>contact</li></ul>
    <h3 style="left:236px">Take Action</h3>
    <ul class="links" style="left:242px"><li>Donate</li><li>More Ways To Give</li></ul>
    <h3 style="left:420px">Our Work</h3>
    <ul class="links" style="left:426px"><li>Support Anti Gun Violence</li><li>Help Disaster Victims</li><li>Help Child Society</li><li>More...</li></ul>
    <h3 style="left:606px">Find Location Nearby</h3>
    <div class="abs zip">zip code</div>
    <div class="abs search">Search</div>
    <p class="abs phone" style="top:80px">TOLL FREE: (855) 555-0142</p>
    <p class="abs phone" style="top:100px">NEW YORK: 518-555-0187</p>
    <h3 style="left:606px;top:137px">Connect</h3>
    <div class="abs social"><span></span><span></span><span></span><span></span>
      <svg width="34" height="34" viewBox="0 0 34 34" aria-label="Email"><circle cx="17" cy="17" r="17" fill="#8ec16d"/><rect x="9" y="11" width="16" height="12" fill="none" stroke="#b9dba0" stroke-width="1.6"/><path d="M9 11l8 7 8-7" fill="none" stroke="#b9dba0" stroke-width="1.6"/></svg>
    </div>
    <p class="abs quote">“True charity is the desire to be useful to others with no thought of recompense.”</p>
    <div class="abs rule"></div>
    <p class="abs legal">Terms &amp; Conditions • Privacy Policy • ©Brightwell Giving 2016 • All Rights Reserved.</p>
  </footer>

</div>
</body>
</html>
```